Bref créative
BrightPath Fuel
Eye Catching Card & Letterhead Design
Professional
Marcus Torres
CEO
4183 HAWTHORNE AVE
SUITE 310
SARASOTA FL 34519
mtorres@brightpathfuel.example
www.brightpathfuel.example
use the WELL portion of the logo and list the twitter site (@brightpathfuel)

```html
<!DOCTYPE html>
<html lang="en">
<head>
<meta charset="utf-8">
<title>BrightPath Fuel – Business Cards</title>
<link href="https://fonts.googleapis.com/css2?family=Open+Sans:wght@400;700&display=swap" rel="stylesheet">
<style>
  :root{
    --stage:#eceae6;
    --card:#ffffff;
    --green-light:#a6cc3c;
    --green-dark:#5f8f17;
    --ink:#3a3a3a;
    --line:#1a1a1a;
    --on-green:#ffffff;
  }
  *{box-sizing:border-box;margin:0;padding:0}
  html,body{width:1200px;height:852px;overflow:hidden}
  body{background:var(--stage);font-family:"Open Sans",Arial,sans-serif;position:relative}
  .card{position:absolute;width:520px;height:300px;border-radius:18px;overflow:hidden;background:var(--card);box-shadow:0 2px 6px rgba(0,0,0,.12)}
  .card--front{left:90px;top:110px}
  .card--back{left:590px;top:440px}
  .card-bg{position:absolute;inset:0;width:100%;height:100%}
  .contact{position:absolute;color:var(--on-green);font-size:10px;line-height:1.45}
  .contact .name{font-weight:700;font-size:14px;line-height:1.2}
  .contact .role{font-size:10px;margin-bottom:60px}
  .contact .address{margin-bottom:12px}
  .contact .row{display:flex;align-items:center;gap:6px}
  .contact .row svg{width:9px;height:9px;flex:none}
  .card--front .contact{left:28px;top:36px}
  .card--back .contact{right:30px;top:36px;text-align:right}
  .card--back .contact .row{justify-content:flex-end;flex-direction:row-reverse}
  .wordmark{position:absolute;display:flex;align-items:center;justify-content:center;gap:8px;color:var(--ink);font-weight:700;font-size:22px;letter-spacing:.3px;white-space:nowrap}
  .wordmark .dot{width:14px;height:14px;border-radius:50%;background:var(--green-dark);flex:none}
  .card--front .wordmark{left:272px;width:232px;top:132px}
  .card--back .wordmark{left:18px;width:248px;top:150px}
</style>
</head>
<body>

<section class="card card--front">
  <svg class="card-bg" viewBox="0 0 520 300" aria-hidden="true">
    <defs>
      <radialGradient id="greenFront" cx="30%" cy="35%" r="75%">
        <stop offset="0" stop-color="var(--green-light)"/>
        <stop offset="1" stop-color="var(--green-dark)"/>
      </radialGradient>
    </defs>
    <path d="M0 0 H215 C285 70 170 200 255 300 H0 Z" fill="url(#greenFront)"/>
    <path d="M222 0 C294 72 180 200 264 300" fill="none" stroke="var(--line)" stroke-width="3"/>
  </svg>
  <div class="contact">
    <p class="name">Marcus Torres</p>
    <p class="role">CEO</p>
    <p class="address">4183 Hawthorne AVE Suite 310<br>Sarasota FL 34519</p>
    <p class="row"><svg viewBox="0 0 10 10"><path d="M2 0.5h2l1 2.5-1.4 1a5 5 0 0 0 2.4 2.4l1-1.4 2.5 1v2a1 1 0 0 1-1 1A8.5 8.5 0 0 1 1 1.5a1 1 0 0 1 1-1z" fill="currentColor"/></svg>407.555.0192</p>
    <p class="row"><svg viewBox="0 0 10 10"><rect x="0.5" y="2" width="9" height="6" fill="currentColor"/><path d="M0.5 2l4.5 3.5L9.5 2" fill="none" stroke="#6e9a1c" stroke-width="0.8"/></svg>mtorres@brightpathfuel.example</p>
    <p class="row"><svg viewBox="0 0 10 10"><circle cx="5" cy="5" r="4.3" fill="none" stroke="currentColor" stroke-width="1"/><path d="M0.7 5h8.6M5 0.7c-2.4 2.6-2.4 5.9 0 8.6M5 0.7c2.4 2.6 2.4 5.9 0 8.6" fill="none" stroke="currentColor" stroke-width="0.8"/></svg>www.brightpathfuel.example</p>
    <p class="row"><svg viewBox="0 0 10 10"><circle cx="5" cy="5" r="4.3" fill="currentColor"/></svg>@brightpathfuel</p>
  </div>
  <div class="wordmark"><span class="dot"></span>BrightPath Fuel</div>
</section>

<section class="card card--back">
  <svg class="card-bg" viewBox="0 0 520 300" aria-hidden="true">
    <defs>
      <radialGradient id="greenBack" cx="75%" cy="40%" r="75%">
        <stop offset="0" stop-color="var(--green-light)"/>
        <stop offset="1" stop-color="var(--green-dark)"/>
      </radialGradient>
    </defs>
    <path d="M520 0 H300 C245 80 355 190 285 300 H520 Z" fill="url(#greenBack)"/>
    <path d="M292 0 C237 80 347 190 277 300" fill="none" stroke="var(--line)" stroke-width="3"/>
  </svg>
  <div class="contact">
    <p class="name">Marcus Torres</p>
    <p class="role">CEO</p>
    <p class="address">4183 Hawthorne AVE Suite 310<br>Sarasota FL 34519</p>
    <p class="row"><svg viewBox="0 0 10 10"><path d="M2 0.5h2l1 2.5-1.4 1a5 5 0 0 0 2.4 2.4l1-1.4 2.5 1v2a1 1 0 0 1-1 1A8.5 8.5 0 0 1 1 1.5a1 1 0 0 1 1-1z" fill="currentColor"/></svg>407.555.0192</p>
    <p class="row"><svg viewBox="0 0 10 10"><rect x="0.5" y="2" width="9" height="6" fill="currentColor"/><path d="M0.5 2l4.5 3.5L9.5 2" fill="none" stroke="#6e9a1c" stroke-width="0.8"/></svg>mtorres@brightpathfuel.example</p>
    <p class="row"><svg viewBox="0 0 10 10"><circle cx="5" cy="5" r="4.3" fill="none" stroke="currentColor" stroke-width="1"/><path d="M0.7 5h8.6M5 0.7c-2.4 2.6-2.4 5.9 0 8.6M5 0.7c2.4 2.6 2.4 5.9 0 8.6" fill="none" stroke="currentColor" stroke-width="0.8"/></svg>www.brightpathfuel.example</p>
    <p class="row"><svg viewBox="0 0 10 10"><circle cx="5" cy="5" r="4.3" fill="currentColor"/></svg>@brightpathfuel</p>
  </div>
  <div class="wordmark"><span class="dot"></span>BrightPath Fuel</div>
</section>

</body>
</html>
```